Life Coaching stationery
Harbour Crest Coaching
Project: Life Coaching stationery
Life Coaching stationery -
Creative Brief
Professional
Marisa Dowd-Fenwick BForSci
Life & Career Coach
marisa@harbourcrestcoaching.co.nz
www.harbourcrestcoaching.co.nz
Also need letterhead, thanks.

```html
<!DOCTYPE html>
<html lang="en">
<head>
<meta charset="utf-8">
<title>Harbour Crest Coaching – Business Card</title>
<link rel="stylesheet" href="https://fonts.googleapis.com/css2?family=PT+Sans:ital,wght@0,400;0,700;1,400&display=swap">
<style>
  :root {
    --page-bg: #e4e9ef;
    --card-bg: #ffffff;
    --brand-navy: #123f7a;
    --brand-blue: #1c6db4;
    --text-grey: #5f6670;
    --rule-blue: #2f7fc6;
    --mark-blue: #1a5aa3;
    --ghost-grey: #eef0f2;
  }
  * { margin: 0; padding: 0; box-sizing: border-box; }
  html, body {
    width: 1200px;
    height: 931px;
    overflow: hidden;
    background: var(--page-bg);
    font-family: "PT Sans", Arial, sans-serif;
  }
  .business-card {
    position: absolute;
    left: 105px;
    top: 160px;
    width: 990px;
    height: 572px;
    background: var(--card-bg);
    overflow: hidden;
  }
  .ghost-disc {
    position: absolute;
    left: 755px;
    top: 240px;
    width: 350px;
    height: 350px;
    border-radius: 50%;
    background: var(--ghost-grey);
  }
  .brand-mark {
    position: absolute;
    left: 42px;
    top: 55px;
    width: 180px;
    height: 180px;
    border-radius: 50%;
    background: var(--mark-blue);
  }
  .brand-lockup {
    position: absolute;
    left: 250px;
    top: 150px;
    display: inline-flex;
    flex-direction: column;
    align-items: flex-end;
  }
  .brand-name {
    font-size: 42px;
    line-height: 46px;
    font-weight: 400;
    color: var(--brand-navy);
    white-space: nowrap;
    letter-spacing: -0.5px;
  }
  .brand-tagline {
    margin-top: 2px;
    font-size: 17px;
    line-height: 20px;
    font-style: italic;
    color: var(--brand-navy);
    white-space: nowrap;
  }
  .person-name {
    position: absolute;
    left: 93px;
    top: 326px;
    font-size: 28px;
    color: var(--brand-blue);
  }
  .person-role {
    position: absolute;
    left: 93px;
    top: 364px;
    font-size: 21px;
    color: var(--text-grey);
  }
  .contact-list {
    position: absolute;
    left: 93px;
    top: 436px;
    list-style: none;
    font-size: 21px;
    color: var(--text-grey);
    line-height: 33px;
  }
  .contact-label {
    font-weight: 700;
    color: var(--brand-blue);
  }
  .footer-rule {
    position: absolute;
    left: 0;
    right: 0;
    top: 517px;
    height: 2px;
    background: var(--rule-blue);
  }
  .website {
    position: absolute;
    left: 95px;
    top: 528px;
    font-size: 23px;
    letter-spacing: 0.34em;
    color: var(--brand-navy);
  }
</style>
</head>
<body>
  <main class="business-card">
    <div class="ghost-disc" aria-hidden="true"></div>

    <div class="brand-mark" aria-hidden="true"></div>
    <div class="brand-lockup">
      <p class="brand-name">Harbour Crest Coaching</p>
      <p class="brand-tagline">Steady course for growth</p>
    </div>

    <p class="person-name">Marisa Dowd-Fenwick BForSci</p>
    <p class="person-role">Life &amp; Career Coach</p>

    <ul class="contact-list">
      <li><span class="contact-label">C:</span> 021 387 604</li>
      <li><span class="contact-label">E:</span> marisa@harbourcrestcoaching.co.nz</li>
    </ul>

    <div class="footer-rule" aria-hidden="true"></div>
    <p class="website">www.harbourcrestcoaching.co.nz</p>
  </main>
</body>
</html>
```